brightleafwell.com and taverclinic.com

I'd like to do a web design re-make on two of our websites. Brightleafwell.com is focused on selling nutriceutical products (private labeled by brightleafwell.com), and provide an expert blog to give great advices on general health.

Taverclinic.com is a site for Dr. Taver's new medicine clinic. It should be integrated with brightleafwell.com. Clients can directly make appointments on the site, and order products from brightleafwell.com.

Target Market(s)

Middle to upper

Industry/Entity Type

Clinic

Number of Pages Required

4 page

Font styles to use
Serif
Sans Serif

Colors
0254a3
0792cd
33a6d7
00a98f
33b7a4
acd036
9bcb3c
cadf82

Requirements
Must have
• Home page tabs: About Dr. Taver, Store, Blog, Videos, Appointment
• Home page content should include: a promotional section (with moving features), an appointment book (for online appointment booking), a product section (for store), and a blog section.
Nice to have
• The look and feel should be modern, professional, trustworthy, zen.
Should not have
• Real pictures of people, except for Dr. Taver.

```html
<!DOCTYPE html>
<html lang="en">
<head>
<meta charset="utf-8">
<title>brightleafwell — Dr. Taver</title>
<link href="https://fonts.googleapis.com/css2?family=Baloo+2:wght@600;700&family=Roboto:wght@400;500&display=swap" rel="stylesheet">
<style>
  :root {
    --page-bg: #e4e4df;
    --panel: #ffffff;
    --hero-green: #cce045;
    --logo-green: #8fcd4b;
    --cta-green: #6ad112;
    --tick-green: #5fbf1a;
    --section-bg: #f5f5f5;
    --ink: #222222;
    --ink-soft: #333333;
    --link-blue: #1a7cc6;
    --line: #dcdcdc;
  }
  * { box-sizing: border-box; margin: 0; padding: 0; }
  html, body { width: 1200px; height: 989px; overflow: hidden; }
  body {
    background: var(--page-bg);
    font-family: "Roboto", Arial, sans-serif;
    color: var(--ink);
    position: relative;
  }
  .site {
    position: absolute; left: 77px; top: 45px;
    width: 1057px; height: 944px;
    background: var(--panel);
    overflow: hidden;
  }
  .topbar {
    position: absolute; left: 0; top: 0; width: 100%; height: 41px;
    background: var(--panel);
  }
  .brand {
    position: absolute; left: 90px; top: 7px;
    font-family: "Baloo 2", sans-serif; font-weight: 600;
    font-size: 21px; letter-spacing: 1px; color: var(--logo-green);
    line-height: 28px;
  }
  .main-nav {
    position: absolute; right: 91px; top: 0; height: 41px;
    display: flex; gap: 27px; align-items: center;
    font-size: 14px; color: var(--ink);
  }
  .main-nav a { color: inherit; text-decoration: none; }

  .hero {
    position: absolute; left: 0; top: 41px; width: 100%; height: 525px;
    background: var(--hero-green);
    overflow: hidden;
  }
  .hero-produce {
    position: absolute; left: 0; top: 219px; width: 490px; height: 306px;
    border-top-right-radius: 60% 75%;
    border-top-left-radius: 10% 30%;
    background:
      radial-gradient(circle at 75% 40%, #e8622a 0%, rgba(232,98,42,0) 40%),
      radial-gradient(circle at 30% 55%, #c8321c 0%, rgba(200,50,28,0) 45%),
      linear-gradient(160deg, #b8501f 0%, #d8421f 45%, #e8772b 100%);
  }
  .hero-title {
    position: absolute; left: 0; top: 112px; width: 100%;
    text-align: center; color: #fff;
    font-family: "Baloo 2", sans-serif; font-weight: 700;
    font-size: 84px; line-height: 90px; letter-spacing: -0.5px;
  }
  .hero-sub {
    position: absolute; left: 0; top: 305px; width: 100%;
    text-align: center; color: #fff; font-size: 18px;
  }
  .btn-primary {
    position: absolute; left: 445px; top: 345px;
    width: 167px; height: 43px; border-radius: 22px;
    background: var(--cta-green); color: #fff;
    font-size: 14px; font-weight: 500;
    display: flex; align-items: center; justify-content: center;
    text-decoration: none;
  }

  .about {
    position: absolute; left: 0; top: 566px; width: 100%; height: 378px;
    background: var(--section-bg);
  }
  .about-heading {
    position: absolute; left: 0; top: 42px; width: 100%;
    text-align: center; font-size: 18px; font-weight: 400; color: var(--ink);
  }
  .portrait {
    position: absolute; left: 90px; top: 104px;
    width: 124px; height: 124px; border-radius: 50%;
    background: #fff; border: 1px solid var(--line);
  }
  .portrait-fill {
    position: absolute; left: 7px; top: 7px; width: 108px; height: 108px;
    border-radius: 50%;
    background: radial-gradient(circle at 50% 45%, #d9b6a3 0%, #6a5a4e 55%, #2b2b2b 100%);
  }
  .bio {
    position: absolute; left: 235px; top: 148px; width: 730px;
    font-size: 14px; line-height: 18px; color: var(--ink-soft);
  }
  .bio-name { font-size: 17px; color: var(--ink); }
  .bio-lead { margin-top: 14px; font-weight: 500; color: var(--ink); }
  .credentials { list-style: none; margin-top: 18px; }
  .credentials li { display: flex; align-items: center; gap: 5px; height: 21.5px; }
  .credentials svg { width: 11px; height: 11px; flex: none; }
  .btn-outline {
    position: absolute; left: 445px; top: 331px;
    width: 167px; height: 43px; border-radius: 22px;
    border: 1px solid var(--line); background: var(--section-bg);
    color: var(--link-blue); font-size: 14px; font-weight: 500;
    display: flex; align-items: center; justify-content: center;
    text-decoration: none;
  }
</style>
</head>
<body>
  <div class="site">
    <header class="topbar">
      <div class="brand">BRIGHTLEAFWELL</div>
      <nav class="main-nav">
        <a href="#">Make an appointment with Dr. Taver</a>
        <a href="#">Store</a>
        <a href="#">Expert Blog</a>
        <a href="#">Videos</a>
        <a href="#">Contact</a>
      </nav>
    </header>

    <section class="hero">
      <div class="hero-produce" role="img" aria-label="Pile of fresh red fruit and vegetables: peppers, tomatoes, apples, grapes and strawberries"></div>
      <h1 class="hero-title">empowering your angeless<br>body and mind.</h1>
      <p class="hero-sub">Feel young, look beautiful, filled with energy, free of pain, be happy and joyful!</p>
      <a class="btn-primary" href="#">See more about us</a>
    </section>

    <section class="about">
      <h2 class="about-heading">Welcome to brightleafwell, a little story about us.</h2>
      <div class="portrait">
        <div class="portrait-fill" role="img" aria-label="Portrait photo of Dr. Taver Lane"></div>
      </div>
      <div class="bio">
        <p><span class="bio-name">Dr. Taver Lane,</span> as thousands of patients refer to as “Dr Taver” or “the Healer”, brings a great combination between modern medical sciences and ancient medicine. Every smile, hug and encouraging word from her in addition to her sincerely caring and loving nature give those in need tremendous healing power!</p>
        <p class="bio-lead">Here’s a brief introduction for Dr Taver Lane’s background:</p>
        <ul class="credentials">
          <li><svg viewBox="0 0 12 12"><path d="M1.5 6.5 4.5 9.5 10.5 2.5" fill="none" stroke="var(--tick-green)" stroke-width="2.4" stroke-linecap="round" stroke-linejoin="round"/></svg>M.D. from Northfield University, Clinical Medicine</li>
          <li><svg viewBox="0 0 12 12"><path d="M1.5 6.5 4.5 9.5 10.5 2.5" fill="none" stroke="var(--tick-green)" stroke-width="2.4" stroke-linecap="round" stroke-linejoin="round"/></svg>M.S. from Harborview University,Medical Human Physiology</li>
          <li><svg viewBox="0 0 12 12"><path d="M1.5 6.5 4.5 9.5 10.5 2.5" fill="none" stroke="var(--tick-green)" stroke-width="2.4" stroke-linecap="round" stroke-linejoin="round"/></svg>Post Doctor Research Associate, University of Westmesa, Cancer Center</li>
          <li><svg viewBox="0 0 12 12"><path d="M1.5 6.5 4.5 9.5 10.5 2.5" fill="none" stroke="var(--tick-green)" stroke-width="2.4" stroke-linecap="round" stroke-linejoin="round"/></svg>PhD Oriental Medicine</li>
        </ul>
      </div>
      <a class="btn-outline" href="#">Make an appointment</a>
    </section>
  </div>
</body>
</html>
```